New letter head for Air Conditioning business

We need a new professional letter head design to suit our new re-branded air conditioning business. Our new logo is attached

```html
<!DOCTYPE html>
<html lang="en">
<head>
<meta charset="utf-8">
<title>Northwind Letterhead</title>
<link href="https://fonts.googleapis.com/css2?family=Open+Sans:wght@400;600;700&display=swap" rel="stylesheet">
<style>
  :root {
    --backdrop: #e9e1d3;
    --paper: #fbfbfa;
    --ink: #2f2f2f;
    --ink-soft: #454545;
    --brand-green: #2bab4a;
    --brand-red: #e2362b;
    --signature-tone: #d9d9d9;
  }
  * { margin: 0; padding: 0; box-sizing: border-box; }
  html, body {
    width: 1200px;
    height: 800px;
    overflow: hidden;
    background: var(--backdrop);
    font-family: "Open Sans", sans-serif;
    color: var(--ink);
  }
  .letterhead {
    position: absolute;
    left: 331px;
    top: 20px;
    width: 537px;
    height: 760px;
    background: var(--paper);
    box-shadow: 0 2px 10px rgba(0,0,0,0.08);
  }
  .block { position: absolute; left: 60px; }
  .brand {
    top: 30px;
    display: flex;
    align-items: center;
    gap: 12px;
  }
  .brand-dot {
    width: 38px;
    height: 38px;
    border-radius: 50%;
    background: var(--ink);
  }
  .brand-name {
    font-size: 22px;
    font-weight: 700;
    letter-spacing: 3px;
    color: var(--ink);
  }
  .date { top: 104px; font-size: 11px; }
  .recipient { top: 132px; font-size: 11px; line-height: 13.6px; }
  .salutation { top: 239px; font-size: 11px; font-weight: 700; }
  .body-copy {
    width: 424px;
    font-size: 10.6px;
    line-height: 14.4px;
    text-align: justify;
    hyphens: auto;
    color: var(--ink-soft);
  }
  .para-1 { top: 281px; }
  .para-2 { top: 382px; }
  .para-3 { top: 469px; }
  .closing { top: 571px; font-size: 10px; color: var(--ink-soft); }
  .signature {
    top: 592px;
    width: 120px;
    height: 26px;
    border-radius: 4px;
    background: linear-gradient(90deg, var(--signature-tone), rgba(217,217,217,0.35));
  }
  .signer { top: 626px; font-size: 11px; font-weight: 600; letter-spacing: -0.2px; }
  .signer-company { top: 641px; font-size: 10.5px; color: var(--ink-soft); letter-spacing: -0.2px; }
  .contact { top: 697px; font-size: 9.6px; line-height: 12.6px; color: var(--ink); }
  .contact-company { color: var(--brand-green); }
  .label { color: var(--brand-red); }
</style>
</head>
<body>
  <main class="letterhead">
    <header class="block brand">
      <span class="brand-dot"></span>
      <span class="brand-name">NORTHWIND</span>
    </header>

    <p class="block date">10 September, 2020</p>

    <address class="block recipient" style="font-style: normal;">
      Mr, Daniel R.Whitcombe<br>
      President<br>
      BR Holdings<br>
      2207 Maplecrest Ln; Ashford,<br>
      VA 22950-1184
    </address>

    <p class="block salutation">Dear Mr,Daniel</p>

    <p class="block body-copy para-1">Contrary to popular belief, Lorem Ipsum is not simply random text. It has roots in a piece of classical Latin literature from 45 BC, making it over 2000 years old. Peter Alwood, a Latin professor at Hollins Ridge College in Virginia, looked up one of the more obscure Latin words, consectetur, from a Lorem Ipsum passage, and going through the cites of the word in classical literature, discovered the undoubtable source.</p>

    <p class="block body-copy para-2">Lorem Ipsum comes from sections 1.10.32 and 1.10.33 of "de Finibus Bonorum et Malorum" (The Extremes of Good and Evil) by Cicero, written in 45 BC. This book is a treatise on the theory of ethics, very popular during the Renaissance. Lorem Ipsum used since the 1500s is reproduced below for those interested. Sections 1.10.32 and 1.10.33 from "de Finibus Bonorum et Malorum" by Cicero are also reproduced in</p>

    <p class="block body-copy para-3">Contrary to popular belief, Lorem Ipsum is not simply random text. It has roots in a piece of classical Latin literature from 45 BC, making it over 2000 years old. Peter Alwood, a Latin professor at Hollins Ridge College in Virginia, looked up one of the more obscure Latin words.</p>

    <p class="block closing">Sincerely your</p>
    <div class="block signature" role="img" aria-label="Handwritten signature"></div>
    <p class="block signer">Owen M. Prescott</p>
    <p class="block signer-company">Company name</p>

    <footer class="block contact">
      <span class="contact-company">NORTHWIND AIR CONDITIONING &amp; REFRIGERATION</span><br>
      4870 Ridgeview Rd; Dalton,<br>
      <span class="label">Tel</span>:(555)210-4471 <span class="label">Fex</span>:(555)210-4472<br>
      <span class="label">Email</span>:hello@northwindair.example
    </footer>
  </main>
</body>
</html>
```